MOSLEN Environmental needs an upgrade to its current business cards design

We need an upgrade to our current business cards design, where the MOSLEN acronym is included, as possible and not being overloaded.
MOSLEN Environmental is an Environmental Consultancy Firm based in Sydney.
We would like to see creative designs different from the standard type of business cards (for example, rounded edges, different to standard size of common business cards.

Target Market(s)

industrial companies (oil & gas, petrochemical, mining, insolvency, finance and manufacturing), developers, architect firms, law firms.

Industry/Entity Type

Business

Contact Information for Business Card

logos (brand and acronym), if they don't appear overloaded.
name
role
name of company (MOSLEN Environmental),
address (Level 3, Suite 3C, 47-49 Dorrigan Lane, Wexmoor, NSW, 2188) landline (02 7314 2986)
mobile (staff member)
email (staff member) and
website (www.moslengreen.example).
Include: Contaminated Land, Site Remediation, Groundwater Assessment, Health and Ecological Risk Assessments, Acid Sulfate Soils, Waste Classification.

Font styles to use
Serif
Sans Serif

Requirements
Must have
• A creative design different to the standard type of business cards.
Nice to have
• Rounded edges
• Different size of business cards rather than the standard size.
Should not have
• Preferable not to use white colour background, unless it is required from a creative design proposed.
• Not an overloaded design.
• Avoid black colours

```html
<!DOCTYPE html>
<html lang="en">
<head>
<meta charset="utf-8">
<title>MOSLEN Environmental – Business Card</title>
<link rel="stylesheet" href="https://fonts.googleapis.com/css2?family=Open+Sans:wght@400;600;800&display=swap">
<style>
  :root {
    --stage: #000000;
    --leaf-green: #4f9e36;
    --forest: #1d4f3a;
    --white: #ffffff;
    --rule: rgba(255,255,255,0.35);
  }
  html, body {
    margin: 0;
    padding: 0;
    width: 1200px;
    height: 900px;
    overflow: hidden;
    background: var(--stage);
  }
  .card-sheet {
    display: block;
    width: 1200px;
    height: 900px;
    font-family: "Open Sans", sans-serif;
  }
  .front-face { fill: var(--leaf-green); }
  .back-face { fill: var(--forest); }
  .band-area { fill: var(--forest); }
  .text-white { fill: var(--white); }
  .brand-name { font-weight: 800; font-size: 58px; letter-spacing: 1px; }
  .brand-sub { font-weight: 800; font-size: 20px; letter-spacing: 3.2px; }
  .brand-sub-large { font-size: 20.5px; letter-spacing: 4px; }
  .person-name { font-size: 29px; font-weight: 400; letter-spacing: 0.5px; }
  .person-role { font-size: 21px; font-weight: 400; letter-spacing: 0.3px; }
  .contact-line { font-size: 21.5px; font-weight: 400; letter-spacing: 0.3px; }
  .service-item { font-size: 22px; font-weight: 400; letter-spacing: 0.4px; }
  .divider { stroke: var(--white); stroke-width: 1.5; }
  .service-rule { stroke: var(--rule); stroke-width: 1.5; }
  .icon { fill: var(--white); }
  .icon-stroke { fill: none; stroke: var(--white); stroke-width: 1.6; }
</style>
</head>
<body>
<svg class="card-sheet" viewBox="0 0 1200 900" xmlns="http://www.w3.org/2000/svg">
  <defs>
    <clipPath id="front-clip">
      <path d="M185,38 H950 Q1000,110 1040,220 Q1078,330 1050,435 H185 Q160,435 160,410 V63 Q160,38 185,38 Z"/>
    </clipPath>
    <clipPath id="back-clip">
      <path d="M262,468 H1018 Q1043,468 1043,493 V841 Q1043,866 1018,866 H148 Q118,760 150,640 Q188,522 262,468 Z"/>
    </clipPath>
    <linearGradient id="side-art-tone" x1="0" y1="0" x2="1" y2="0">
      <stop offset="0" stop-color="#4f9e36"/>
      <stop offset="0.7" stop-color="#3f8a34"/>
      <stop offset="1" stop-color="#1d4f3a"/>
    </linearGradient>
  </defs>

  <!-- Front card -->
  <g class="front-card">
    <path class="front-face" d="M185,38 H950 Q1000,110 1040,220 Q1078,330 1050,435 H185 Q160,435 160,410 V63 Q160,38 185,38 Z"/>
    <g clip-path="url(#front-clip)">
      <rect class="band-area" role="img" aria-label="Dark green pipe illustration band" x="318" y="80" width="800" height="42"/>
    </g>

    <g class="brand-block text-white">
      <text class="brand-name" x="342" y="284" text-anchor="middle">MOSLEN</text>
      <text class="brand-sub" x="342" y="313" text-anchor="middle">ENVIRONMENTAL</text>
    </g>

    <g class="identity text-white">
      <text class="person-name" x="598" y="176">NOLAN VESIK</text>
      <text class="person-role" x="598" y="209">PROJECT ENGINEER</text>
    </g>
    <line class="divider" x1="598" y1="224" x2="1045" y2="224"/>

    <g class="contact-details text-white">
      <text class="contact-line" x="598" y="259">Level 3, Suite 3C, 47-49</text>
      <text class="contact-line" x="598" y="289">Dorrigan Lane, Wexmoor, NSW, 2188</text>
      <text class="contact-line" x="598" y="328">02 7314 2986</text>
      <text class="contact-line" x="598" y="361">0431 587 206</text>
      <text class="contact-line" x="598" y="395">nolan@moslengreen.example</text>
      <text class="contact-line" x="236" y="395">www.moslengreen.example</text>
    </g>

    <path class="icon" d="M573,242 a6,6 0 0 1 6,6 c0,5 -6,12 -6,12 c0,0 -6,-7 -6,-12 a6,6 0 0 1 6,-6 z M573,245.5 a2.5,2.5 0 1 0 0.01,0 z" fill-rule="evenodd"/>
    <g class="icon">
      <path d="M562,316 q11,-6 22,0 v4 h-5 v-2 q-6,-2 -12,0 v2 h-5 z"/>
      <rect x="565" y="321" width="16" height="9" rx="2"/>
    </g>
    <path class="icon" d="M566,344 q3,-2 5,0 l2,4 q0,2 -2,3 q2,4 6,6 q1,-2 3,-2 l4,2 q2,2 0,5 q-3,3 -7,2 q-9,-3 -13,-12 q-1,-5 2,-8 z"/>
    <g>
      <rect class="icon" x="564" y="381" width="19" height="13" rx="1"/>
      <path d="M564,382 L573.5,389 L583,382" fill="none" stroke="#4f9e36" stroke-width="1.6"/>
    </g>
    <g>
      <circle class="icon-stroke" cx="216" cy="387" r="8"/>
      <ellipse class="icon-stroke" cx="216" cy="387" rx="3.5" ry="8"/>
      <line class="icon-stroke" x1="208" y1="387" x2="224" y2="387"/>
    </g>
  </g>

  <!-- Back card -->
  <g class="back-card">
    <path class="back-face" d="M262,468 H1018 Q1043,468 1043,493 V841 Q1043,866 1018,866 H148 Q118,760 150,640 Q188,522 262,468 Z"/>
    <g clip-path="url(#back-clip)">
      <rect role="img" aria-label="Large green leaf illustration" fill="url(#side-art-tone)" x="120" y="468" width="250" height="398"/>
    </g>

    <g class="brand-block text-white">
      <text class="brand-name" x="512" y="674" text-anchor="middle">MOSLEN</text>
      <text class="brand-sub brand-sub-large" x="518" y="712" text-anchor="middle">ENVIRONMENTAL</text>
    </g>

    <g class="service-list text-white">
      <text class="service-item" x="695" y="553">Contaminated Land</text>
      <text class="service-item" x="695" y="596">Site Remediation</text>
      <text class="service-item" x="695" y="639">Groundwater Assessment</text>
      <text class="service-item" x="695" y="682">Health and Ecological</text>
      <text class="service-item" x="695" y="712">Risk Assessments</text>
      <text class="service-item" x="695" y="755">Acid Sulfate Soils</text>
      <text class="service-item" x="695" y="798">Waste Classification.</text>
    </g>
    <g class="service-rules">
      <line class="service-rule" x1="693" y1="567" x2="1040" y2="567"/>
      <line class="service-rule" x1="693" y1="610" x2="1040" y2="610"/>
      <line class="service-rule" x1="693" y1="653" x2="1040" y2="653"/>
      <line class="service-rule" x1="693" y1="726" x2="1040" y2="726"/>
      <line class="service-rule" x1="693" y1="769" x2="1040" y2="769"/>
    </g>
  </g>
</svg>
</body>
</html>
```